Packaging Label for Cloth Diaper Products | ||
BumbleNest Cloth Diaper | ||
The wrap you fold already folds its own way | ||
1. What we have: A 20CM x 25CM package bag. The front side of the bag is seeing through plastic and the back side of the bag is non-woven fabric. 2. What we need: Three graphic designs: Design One (The back side of the package bag) --------------------------------------------------------------- a) One color pattern which will be printed on non-woven fabric (the back side of the package bag). It must be pattern design, must have BumbleNest brand name and logo. b) Choose color for non-woven fabric (need PANTONE color number) Design Two (The front side of the package bag for cloth diaper product) -------------------------------------------------------------------------------------------- Coloured printed sticker (12cm X 6.5cm or any Rectangle size fits the package better) which will be stick on the plastic front side of the package bag a) Choose background colors for printed sticker b) It should include the following information: i. Brand Name and Logo: BumbleNest Cloth Diaper and BumbleNest logo ii. Tagline: The wrap you fold already folds its own way ™ iii. Size: One Size (8 – 40 lbs) iv. Feature: One diaper can be used as All-In-Two, All-In-Three, Cover, Pocket, and Hybrid. v. Bonus: Includes BumbleNest Liner Sheet Design Three (The front side of the package bag for insert pad product) --------------------------------------------------------------------------------------------- Coloured printed sticker (12cm X 6.5cm or any Rectangle size fits the package better) which will be stick on the plastic front side of the package bag. This is the same size as the Design Two. a) The background colors for printed sticker should be the same as the Design Two. b) It should include the following information: i. Brand Name and Logo: BumbleNest Insert Pad and BumbleNest logo ii.Tagline: The wrap you fold already folds its own way ™ iii. Feature: Soft, Slim, and Absorbent iv. Fabric (check mark): 55% Hemp 45 % Organic Cotton, 100% Organic Cotton, 100% Quick-Dry Polyester |
Children | ||
Young mothers in North America. We are looking for something MODERN, SIMPLE and CUTE – that will have a strong design element. | ||
Please see our logo, package bag, and some samples we like in the link below: http://www.snapvault-example.com/albums/48213907@K02/ |

```html
<!DOCTYPE html>
<html lang="en">
<head>
<meta charset="utf-8">
<title>BumbleNest Packaging Labels</title>
<link rel="stylesheet" href="https://fonts.googleapis.com/css2?family=Questrial&family=Arimo:wght@400;700&display=swap">
<style>
  :root {
    --paper: #ffffff;
    --fabric-yellow: #fbf3a9;
    --fabric-mark: #f47a2a;
    --label-green: #8dc63f;
    --frame-grey: #8a8a8a;
    --panel-grey: #808080;
    --note-yellow: #fff59a;
    --brand-orange: #f26a21;
    --ink-grey: #6d6d6d;
    --caption-ink: #333333;
    --white: #ffffff;
    --dot-blue: #6d7fc0;
    --dot-red: #e0483c;
  }
  * { box-sizing: border-box; margin: 0; padding: 0; }
  html, body { width: 1200px; height: 874px; overflow: hidden; background: var(--paper); }
  .sheet { position: relative; width: 1200px; height: 874px; font-family: "Arimo", sans-serif; }

  /* design one: fabric pattern */
  .fabric-pattern {
    position: absolute; left: 0; top: 0; width: 504px; height: 612px;
    background: var(--fabric-yellow); overflow: hidden;
    padding-top: 14px;
  }
  .pattern-row { display: flex; gap: 52px; height: 54px; align-items: center; white-space: nowrap; }
  .pattern-row:nth-child(even) { padding-left: 86px; }
  .pattern-row:nth-child(odd) { padding-left: 8px; }
  .pattern-mark {
    display: flex; align-items: center; gap: 5px;
    font-family: "Questrial", sans-serif; font-size: 17px; color: var(--fabric-mark);
  }
  .pattern-mark::before {
    content: ""; width: 11px; height: 11px; border-radius: 50%; background: var(--fabric-mark);
  }

  .design-caption {
    position: absolute; font-family: "Arimo", sans-serif; color: var(--caption-ink);
    font-size: 32px; text-align: center;
  }
  .pantone-note { position: absolute; left: 0; width: 504px; top: 684px; text-align: center; font-size: 18px; color: var(--caption-ink); }

  /* labels */
  .label {
    position: absolute; left: 547px; width: 630px;
    background: var(--frame-grey); border-radius: 22px; padding: 14px;
  }
  .label--diaper { top: 16px; height: 340px; }
  .label--insert { top: 456px; height: 355px; }
  .label-body {
    position: relative; width: 100%; height: 100%;
    background: var(--label-green); border-radius: 12px;
    outline: 3px solid var(--white); outline-offset: -8px;
    overflow: hidden;
  }
  .label-title {
    position: absolute; left: 0; right: 0; top: 36px; text-align: center;
    font-family: "Questrial", sans-serif; font-weight: 400; color: var(--white); font-size: 40px;
  }
  .label-tagline {
    position: absolute; left: 0; right: 0; top: 86px; text-align: center;
    font-style: italic; color: var(--ink-grey); font-size: 12px;
  }
  .dot-rule { position: absolute; left: 141px; top: 108px; }
  .feature-text {
    position: absolute; left: 0; right: 0; top: 132px; text-align: center;
    color: var(--white); font-size: 14px; line-height: 1.3;
  }
  .brand-mark {
    position: absolute; display: flex; align-items: center; gap: 6px;
    font-family: "Questrial", sans-serif; color: var(--brand-orange); font-size: 22px;
  }
  .brand-mark::before {
    content: ""; width: 16px; height: 16px; border-radius: 50%; background: var(--brand-orange);
  }
  .size-panel {
    position: absolute; left: 210px; top: 240px; width: 135px; height: 80px;
    background: var(--panel-grey); color: var(--white); border-radius: 4px 4px 0 0;
    padding: 12px 14px; font-size: 20px; line-height: 1.25; text-align: center;
  }
  .bonus-note {
    position: absolute; left: 430px; top: 222px; width: 148px; height: 80px;
    background: var(--note-yellow); border-radius: 4px; padding: 8px 10px;
    color: var(--brand-orange); font-size: 12px; line-height: 1.2; text-align: center;
    outline: 2px solid var(--brand-orange); outline-offset: -5px;
  }
  .bonus-note strong { display: block; font-family: "Questrial", sans-serif; font-weight: 400; font-size: 20px; margin-bottom: 2px; }

  .label--insert .label-title { text-align: left; left: 18px; top: 34px; }
  .label--insert .label-tagline { text-align: left; left: 22px; top: 84px; }
  .label--insert .dot-rule { left: 22px; top: 106px; }

  .benefit-note {
    position: absolute; left: 0; top: 178px; width: 165px; height: 100px;
    background: var(--note-yellow); color: var(--ink-grey);
    display: flex; align-items: center; justify-content: center; text-align: center;
    font-size: 17px; line-height: 1.3; padding: 10px 14px;
    outline: 2px solid var(--brand-orange); outline-offset: -7px;
  }
  .fabric-panel {
    position: absolute; right: 0; top: 150px; width: 262px; height: 177px;
    background: var(--panel-grey); color: var(--white); padding: 18px 14px;
    font-size: 15px; line-height: 1.3;
  }
  .fabric-panel ul { list-style: none; }
  .fabric-panel li { display: flex; gap: 8px; margin-bottom: 4px; }
  .check-box { flex: none; width: 13px; height: 13px; border: 2px solid var(--white); margin-top: 3px; }
</style>
</head>
<body>
<main class="sheet">

  <section class="design design--fabric">
    <div class="fabric-pattern" aria-label="Repeating BumbleNest name pattern on Pantone yellow non-woven fabric">
      <div class="pattern-row"><span class="pattern-mark">BumbleNest</span><span class="pattern-mark">BumbleNest</span><span class="pattern-mark">BumbleNest</span></div>
      <div class="pattern-row"><span class="pattern-mark">BumbleNest</span><span class="pattern-mark">BumbleNest</span><span class="pattern-mark">BumbleNest</span></div>
      <div class="pattern-row"><span class="pattern-mark">BumbleNest</span><span class="pattern-mark">BumbleNest</span><span class="pattern-mark">BumbleNest</span></div>
      <div class="pattern-row"><span class="pattern-mark">BumbleNest</span><span class="pattern-mark">BumbleNest</span><span class="pattern-mark">BumbleNest</span></div>
      <div class="pattern-row"><span class="pattern-mark">BumbleNest</span><span class="pattern-mark">BumbleNest</span><span class="pattern-mark">BumbleNest</span></div>
      <div class="pattern-row"><span class="pattern-mark">BumbleNest</span><span class="pattern-mark">BumbleNest</span><span class="pattern-mark">BumbleNest</span></div>
      <div class="pattern-row"><span class="pattern-mark">BumbleNest</span><span class="pattern-mark">BumbleNest</span><span class="pattern-mark">BumbleNest</span></div>
      <div class="pattern-row"><span class="pattern-mark">BumbleNest</span><span class="pattern-mark">BumbleNest</span><span class="pattern-mark">BumbleNest</span></div>
      <div class="pattern-row"><span class="pattern-mark">BumbleNest</span><span class="pattern-mark">BumbleNest</span><span class="pattern-mark">BumbleNest</span></div>
      <div class="pattern-row"><span class="pattern-mark">BumbleNest</span><span class="pattern-mark">BumbleNest</span><span class="pattern-mark">BumbleNest</span></div>
      <div class="pattern-row"><span class="pattern-mark">BumbleNest</span><span class="pattern-mark">BumbleNest</span><span class="pattern-mark">BumbleNest</span></div>
    </div>
    <p class="design-caption" style="left:0;width:504px;top:640px;">design one</p>
    <p class="pantone-note">(PANTONE yellow 0131C)</p>
  </section>

  <section class="label label--diaper">
    <div class="label-body">
      <h1 class="label-title">BumbleNest Cloth Diaper</h1>
      <p class="label-tagline">the wrap you fold already folds its own way™</p>
      <svg class="dot-rule" width="320" height="10" viewBox="0 0 320 10" aria-hidden="true">
        <line x1="0" y1="5" x2="110" y2="5" stroke="#e0483c" stroke-width="2" stroke-dasharray="2 6"/>
        <circle cx="130" cy="5" r="3" fill="#6d7fc0"/><circle cx="145" cy="5" r="3" fill="#6d7fc0"/>
        <circle cx="160" cy="5" r="3" fill="#6d7fc0"/><circle cx="175" cy="5" r="3" fill="#6d7fc0"/>
        <circle cx="190" cy="5" r="3" fill="#6d7fc0"/>
        <line x1="210" y1="5" x2="320" y2="5" stroke="#e0483c" stroke-width="2" stroke-dasharray="2 6"/>
      </svg>
      <p class="feature-text">One diaper can be used as:<br>All-In-Two, All-In-Three,<br>Cover, Pocket, and Hybrid.</p>
      <div class="brand-mark" style="left:22px;top:250px;">BumbleNest</div>
      <div class="size-panel">one size<br>8-40 lbs</div>
      <div class="bonus-note"><strong>Bonus!</strong>Includes BumbleNest<br>Liner Sheet</div>
    </div>
  </section>
  <p class="design-caption" style="left:547px;width:630px;top:388px;">design two</p>

  <section class="label label--insert">
    <div class="label-body">
      <h1 class="label-title">BumbleNest Insert Pad</h1>
      <p class="label-tagline">the wrap you fold already folds its own way™</p>
      <svg class="dot-rule" width="320" height="10" viewBox="0 0 320 10" aria-hidden="true">
        <line x1="0" y1="5" x2="110" y2="5" stroke="#e0483c" stroke-width="2" stroke-dasharray="2 6"/>
        <circle cx="130" cy="5" r="3" fill="#6d7fc0"/><circle cx="145" cy="5" r="3" fill="#6d7fc0"/>
        <circle cx="160" cy="5" r="3" fill="#6d7fc0"/><circle cx="175" cy="5" r="3" fill="#6d7fc0"/>
        <circle cx="190" cy="5" r="3" fill="#6d7fc0"/>
        <line x1="210" y1="5" x2="320" y2="5" stroke="#e0483c" stroke-width="2" stroke-dasharray="2 6"/>
      </svg>
      <div class="brand-mark" style="right:20px;top:92px;font-size:17px;">BumbleNest</div>
      <div class="benefit-note">Soft, Slim,<br>and Absorbent</div>
      <div class="fabric-panel">
        <ul>
          <li><span class="check-box"></span><span>55% Hemp,<br>45% Organic Cotton</span></li>
          <li><span class="check-box"></span><span>100% Organic Cotton</span></li>
          <li><span class="check-box"></span><span>100% Quick-Dry<br>Polyester</span></li>
        </ul>
      </div>
    </div>
  </section>
  <p class="design-caption" style="left:547px;width:400px;top:826px;">design three</p>

</main>
</body>
</html>
```